Startseiten-Design für Software-Hersteller
Zielgruppe
Wir sind Softwarehersteller aus Berlin und unser Produkt ist eine Software zur Ortung von Fahrzeugen und zur Tourenplanung. Probleme die wir lösen - wo ist mein Auto gerade? Wo war mein Auto vor 1 Woche? Wie sollten meine Fahrer fahren, um möglichst effizient von A nach Z zu kommen?
Darüber hinaus verkaufen wir auch die für die Software notwendigen GPS-Geräte -> hier haben wir verschiedene Modelle im Angebot und ganz unterschiedliche Anschlussmöglichkeiten. Unsere Zielgruppe sind NUR Geschäftskunden: Handwerker, Bauunternehmen, Verlage, Winterdienste etc...
Aufgabenstellung
Vorab:
am besten ist das Projekt für jemanden geeignet, der schon mal eine affengeile Shop-Startseite gemacht hat - es soll mega professionell wirken und die Produkte sollen ins Auge springen. Wir benötigen nur eine Startseite -> Wichtig: den Shop haben wir bereits! Unsere aktuelle Seite findet ihr unter https://shop.vrn-systeme.de/ (ein absoluter Alptraum).
Gestalterisch könnt ihr euch echt austoben - ich denke wir entscheiden uns dann aus dem Bauch heraus. Wir sind generell auch Fans von etwas schlichtem - Hauptsache die Kunden klicken auf den Bestellen Button (dort verlinken wir dann den eigentlichen Shop). Programmiert wird das von unserem Dienstleister.
Die Startseite die wir möchten, sollte folgendes beinhalten:
- wenig Text -> dafür geile moderne Produktfotos mit ästhetischen Preisen (z. B. den Kaufwelle Shop finden wir hammer!)
- auf jeden Fall eine Zeile für unsere Gütesiegel
- selbstverständlich irgendwie an unsere Corporate Identity gehalten sein
- eine Art Pricing Tabelle beinhalten, in der wir die Unterschiede unserer verschiedenen Tarife verständlich an den Kunden bringen (wir haben sowas bereits auf unserer Website - > aber das sieht auch alles ziemlich Altbacken aus: https://www.vrn-systeme.de/gps-fahrzeugortung/gps-ortung-tourenplanung-tarifvergleich/).
- Wir haben insgesamt 4 Hardwaretypen + eine Menge Zubehör. Somit ist die Anzahl der Produkte recht übersichtlich -> rein für das Design könnt ihr euch die Bilder im Dateiupload ziehen und gern auch identische Fotos der Produkte für das Design nutzen.

```html
<!DOCTYPE html>
<html lang="de">
<head>
<meta charset="utf-8">
<title>WegWacht – Compact OBD</title>
<link href="https://fonts.googleapis.com/css2?family=Archivo+Black&family=Montserrat:ital,wght@0,400;0,500;0,600;1,500&display=swap" rel="stylesheet">
<style>
  :root {
    --page-bg: #dedede;
    --ink: #111111;
    --ink-soft: #333333;
    --accent: #d0203a;
    --band: #1c1c1a;
    --band-text: #f2f2f2;
    --rule: #b9b9b9;
    --product-dark: #1f1f1f;
    --product-mid: #3c3c3c;
  }
  * { box-sizing: border-box; margin: 0; padding: 0; }
  html, body { width: 1200px; height: 789px; overflow: hidden; }
  body {
    font-family: "Montserrat", Arial, sans-serif;
    background: var(--page-bg);
    color: var(--ink);
    position: relative;
  }
  .hero {
    position: absolute; inset: 0 0 244px 0;
    background:
      linear-gradient(118deg, transparent 0 30%, rgba(255,255,255,.18) 30% 44%, transparent 44%),
      linear-gradient(118deg, transparent 0 62%, rgba(0,0,0,.04) 62% 76%, transparent 76%),
      var(--page-bg);
    overflow: hidden;
  }
  .site-header {
    position: absolute; left: 55px; right: 55px; top: 22px; height: 72px;
    border-bottom: 1px solid var(--rule);
  }
  .brand { position: absolute; left: 0; top: 8px; display: flex; align-items: center; gap: 8px; }
  .brand-dot { width: 12px; height: 12px; border-radius: 50%; background: var(--accent); }
  .brand-name { font-size: 22px; font-weight: 600; color: var(--ink-soft); }
  .brand-claim { position: absolute; left: 0; top: 46px; font-size: 10px; letter-spacing: .5px; color: var(--ink-soft); }
  .main-nav { position: absolute; right: 0; top: 30px; display: flex; gap: 24px; font-size: 13px; font-weight: 500; }
  .main-nav a { color: var(--ink); text-decoration: none; }

  .offer { position: absolute; left: 133px; top: 150px; z-index: 2; }
  .offer-brand { font-size: 28px; font-style: italic; font-weight: 500; color: var(--ink); line-height: 1; }
  .offer-title { font-family: "Archivo Black", Arial, sans-serif; font-size: 54px; line-height: 1; letter-spacing: .5px; margin-top: 2px; white-space: nowrap; }
  .offer-sub { font-size: 10.5px; font-weight: 600; margin-top: 6px; letter-spacing: .2px; }
  .features { list-style: none; margin-top: 32px; }
  .features li { font-size: 17px; margin-bottom: 11px; }
  .features li::before { content: ">>"; color: var(--accent); font-size: 13px; margin-right: 6px; letter-spacing: -1px; }
  .cta {
    display: inline-block; margin-top: 28px; width: 259px; height: 45px; line-height: 42px;
    border: 1.5px solid var(--accent); color: var(--accent); text-align: center;
    font-size: 19px; font-weight: 600; letter-spacing: 1.5px; text-decoration: none;
  }
  .footnote { position: absolute; left: 125px; top: 522px; font-size: 10px; }

  .product-photo {
    position: absolute; left: 640px; top: 135px; width: 470px; height: 280px;
    border-radius: 22px;
    background: linear-gradient(150deg, var(--product-mid) 0%, var(--product-dark) 65%, #151515 100%);
    box-shadow: 14px 18px 30px rgba(0,0,0,.18);
  }
  .price {
    position: absolute; left: 630px; top: 428px; display: flex; align-items: baseline;
    font-family: "Archivo Black", Arial, sans-serif; color: var(--accent); z-index: 2;
  }
  .price-currency { font-size: 40px; color: #444; margin-right: 6px; }
  .price-amount { font-size: 84px; line-height: 1; }
  .price-mark { font-size: 40px; color: #555; align-self: flex-start; }
  .seal { position: absolute; left: 1058px; top: 440px; width: 112px; height: 62px; background: #f4f4f4; border-radius: 4px; box-shadow: 0 1px 3px rgba(0,0,0,.2); }

  .intro-band {
    position: absolute; left: 0; right: 0; bottom: 0; height: 244px;
    background: var(--band); color: var(--band-text); text-align: center;
  }
  .intro-title { margin-top: 54px; font-size: 19px; font-weight: 500; letter-spacing: 1px; }
  .intro-title::after { content: ""; display: block; width: 190px; height: 1px; background: #777; margin: 10px auto 0; }
  .intro-text { margin-top: 20px; font-size: 17px; }
</style>
</head>
<body>
  <section class="hero">
    <header class="site-header">
      <div class="brand"><span class="brand-dot"></span><span class="brand-name">WegWacht</span></div>
      <div class="brand-claim">BESSER GEHT'S NICHT</div>
      <nav class="main-nav"><a href="#">ÜBER UNS</a><a href="#">SHOP</a><a href="#">KONTAKT</a></nav>
    </header>

    <div class="offer">
      <div class="offer-brand">WegWacht</div>
      <h1 class="offer-title">COMPACT OBD</h1>
      <p class="offer-sub">FAHRZEUGE ORTEN MIT GPS-TRACKER</p>
      <ul class="features">
        <li>Lorem ipsum dolor sit amet</li>
        <li>Sit amet dolor ipsum amet lorem</li>
        <li>Super features!</li>
      </ul>
      <a class="cta" href="#">ZUM PRODUKT</a>
    </div>

    <div class="product-photo" role="img" aria-label="Produktfoto: schwarzer OBD-GPS-Tracker"></div>

    <div class="price">
      <span class="price-currency">€</span><span class="price-amount">11,99</span><span class="price-mark">*</span>
    </div>
    <div class="seal" role="img" aria-label="Gütesiegel Kundenbewertungen"></div>

    <p class="footnote">*Lorem ipsum dolor sit amet lorem ipsum 13,99€</p>
  </section>

  <section class="intro-band">
    <h2 class="intro-title">BESSER GEHT'S NICHT</h2>
    <p class="intro-text">WegWacht ist selbsterklärend und leicht zu bedienen</p>
  </section>
</body>
</html>
```